Business Card Design Project

New Business Card design for Travorel Technology Ltd using new Logo and new Tagline for staffing company.

About us from our website - www.travorel-example.net:

TraVorel is a leading and recognized Electronic Entertainment, Workforce Augmentation, and Project Management solutions provider with clients in Electronic Entertainment, Legal, Technology, Government and other verticals that range in size from start up organizations to Zentora 300 companies. TraVorel is certified as an 8(a) minority and woman owned enterprise, established in 1998.

Target Market(s)

Companies in Electronic Entertainment, Legal, Government and Technology

Industry/Entity Type

Business

Requirements
Must have
• Must include in small letters the following information on back:

Established in 1998
8(a)(w)(e), Cage #7KQW4, DUNS #412306957

Front should have the following:
Dale Merrow
Vice President
5870 Brookhollow Court
Lindenvale, QX 908172
555-318-2046 X 100
555-742-9813 Fax
555-318-2046 Toll Free
name@travorel-example.net

Our Tagline: Connect • Collaborate • Achieve

```html
<!DOCTYPE html>
<html lang="en">
<head>
<meta charset="utf-8">
<title>TraVorel Business Card</title>
<link href="https://fonts.googleapis.com/css2?family=Arimo:wght@400;700&display=swap" rel="stylesheet">
<style>
  :root {
    --backdrop: #f2f2f2;
    --card-black: #000000;
    --card-white: #ffffff;
    --brand-blue: #1565c0;
    --text-dark: #111111;
    --text-light: #ffffff;
  }
  * { margin: 0; padding: 0; box-sizing: border-box; }
  html, body {
    width: 1200px; height: 900px; overflow: hidden;
    background: var(--backdrop);
    font-family: "Arimo", Arial, sans-serif;
  }
  .canvas { position: relative; width: 1200px; height: 900px; }

  .card {
    position: absolute;
    width: 600px; height: 343px;
    border-radius: 16px;
    overflow: hidden;
    background: var(--card-white);
    box-shadow: 0 2px 6px rgba(0,0,0,0.25);
  }

  /* Front */
  .card-front { left: 70px; top: 60px; }
  .front-body {
    position: absolute; left: 0; top: 0; right: 0; height: 288px;
    background: var(--card-black);
  }
  .brand {
    position: absolute; display: flex; align-items: center; gap: 10px;
    color: var(--text-light); font-weight: 700;
  }
  .brand-dot {
    border-radius: 50%; background: var(--brand-blue); flex: none;
  }
  .front-brand { left: 52px; top: 120px; font-size: 46px; }
  .front-brand .brand-dot { width: 22px; height: 22px; }
  .divider {
    position: absolute; left: 300px; top: 20px; width: 3px; height: 250px;
    background: linear-gradient(to bottom, rgba(21,101,192,0), var(--brand-blue) 50%, rgba(21,101,192,0));
  }
  .contact { position: absolute; left: 332px; top: 40px; }
  .contact-name { color: var(--brand-blue); font-weight: 700; font-size: 28px; line-height: 1.05; }
  .contact-title { color: var(--text-light); font-weight: 700; font-size: 22px; line-height: 1.15; }
  .contact-details {
    margin-top: 16px; color: var(--brand-blue);
    font-size: 14px; line-height: 1.3; list-style: none;
  }
  .tagline {
    position: absolute; left: 0; right: 0; bottom: 0; height: 55px;
    display: flex; justify-content: space-around; align-items: center;
    font-weight: 700; font-size: 22px; color: var(--text-dark);
  }

  /* Back */
  .card-back { left: 530px; top: 500px; }
  .established {
    position: absolute; left: 0; right: 0; top: 20px; text-align: center;
    color: var(--brand-blue); font-weight: 700; font-size: 17px;
  }
  .back-band {
    position: absolute; left: 0; right: 0; top: 58px; height: 160px;
    background: var(--card-black);
    display: flex; justify-content: center; align-items: center;
  }
  .back-brand { position: static; font-size: 58px; }
  .back-brand .brand-dot { width: 26px; height: 26px; }
  .credentials {
    position: absolute; left: 0; right: 0; top: 236px; text-align: center;
    color: var(--text-dark); font-weight: 700; font-size: 17px; line-height: 1.2;
    list-style: none;
  }
</style>
</head>
<body>
<main class="canvas">
  <section class="card card-front" aria-label="Business card front">
    <div class="front-body">
      <div class="brand front-brand"><span class="brand-dot"></span><span>TraVorel</span></div>
      <div class="divider"></div>
      <div class="contact">
        <p class="contact-name">Dale Merrow</p>
        <p class="contact-title">Vice President</p>
        <ul class="contact-details">
          <li>5870 Brookhollow Court</li>
          <li>Lindenvale, QX 908172</li>
          <li>555-318-2046 X 100</li>
          <li>555-742-9813 Fax</li>
          <li>555-318-2046 Toll Free</li>
          <li>name@travorel-example.net</li>
        </ul>
      </div>
    </div>
    <div class="tagline">
      <span>Connect</span><span>Collaborate</span><span>Achieve</span>
    </div>
  </section>

  <section class="card card-back" aria-label="Business card back">
    <p class="established">Established in 1998</p>
    <div class="back-band">
      <div class="brand back-brand"><span class="brand-dot"></span><span>TraVorel</span></div>
    </div>
    <ul class="credentials">
      <li>8(a)(w)(e)</li>
      <li>Cage #7KQW4</li>
      <li>DUNS #412306957</li>
    </ul>
  </section>
</main>
</body>
</html>
```